Leading equine advertising company needing three elements designed for an ad design

We have an advertisement design that we need assistance creating three elements (leather tags) that are cohesively designed and go with the overall advertisement design. Please see the highlighted areas.

Leather tags - I want to use complementary colors to 7c4627 for leather tags and use dark stitching. Colors need to be complementary to the leather dividers used in the footer. All three tag designs *MUST* be uniform; meaning - the same colors, same threads on leather stitching, texture/look and feel, etc. Leather tags must have a realistic look and text must be easy to see.

Top Leather Tag: Font: Use Font: Americane Condensed Weight: Bold
Bottom Leather Tags: Use Font: Play Weight: Bold

Please *ONLY* design the (3) elements (leather tags) that are highlighted in the reference picture.

See blank template to use for when you submit the design for leather tags, so we can see in real time how they would look on our current design.

Font styles to use
Sans Serif

Requirements
Must have
• Tags must all use the same colors, textures, and threading for leather. Want leather tags to have a realistic look to them. Please make sure text is easily to see on tags.

```html
<!DOCTYPE html>
<html lang="en">
<head>
<meta charset="utf-8">
<title>Broodmare Sale Ad – Leather Tags</title>
<link rel="stylesheet" href="https://fonts.googleapis.com/css2?family=Montserrat:wght@800&family=Oswald:wght@500;600&family=Play:wght@700&display=swap">
<style>
:root{
  --leather:#7c4627;
  --leather-light:#9a5a33;
  --leather-dark:#5e3219;
  --stitch:#2a1409;
  --paper:#ebe0c6;
  --paper-dark:#ded0ae;
  --ink:#33200f;
  --accent:#c67a3c;
  --wood:#3a2416;
  --wood-dark:#22140b;
  --white:#ffffff;
  --cream:#efe6d2;
}
*{margin:0;padding:0;box-sizing:border-box}
html,body{width:746px;height:1200px;overflow:hidden;background:#fff}
.canvas{position:relative;width:746px;height:1200px;background:#fff}
.tag-sample{position:absolute;overflow:visible}
.tag-top{left:195px;top:34px;width:356px;height:175px}
.tag-left{left:13px;top:245px;width:357px;height:174px}
.tag-right{left:372px;top:245px;width:357px;height:174px}

.ad{position:absolute;left:0;top:454px;width:746px;height:746px;overflow:hidden}
.header{position:absolute;left:0;top:0;width:746px;height:152px;background:linear-gradient(180deg,var(--paper),var(--paper-dark))}
.torn{position:absolute;left:0;top:142px;width:746px;height:14px}
.reg-name{position:absolute;left:12px;top:16px;font:800 22px/1 'Montserrat',sans-serif;color:var(--ink);letter-spacing:-.3px}
.horse-desc{position:absolute;left:12px;top:42px;font:600 15px/1 'Oswald',sans-serif;color:var(--accent)}
.lte{position:absolute;left:12px;font:500 12px/1 'Oswald',sans-serif;color:var(--ink)}
.ped{position:absolute;font:500 11px/1 'Oswald',sans-serif;color:var(--ink);white-space:nowrap}
.ped.parent{right:265px;text-align:right}
.ped.parent.lbl{font-size:12px;font-weight:600}
.ped.gp{left:496px;font-size:11px}
.ped.ggp{left:629px;font-size:9px}
.ped-line{position:absolute;height:1px;background:var(--ink)}

.photo-wrap{position:absolute;left:0;top:148px;width:746px;height:458px;
  background:linear-gradient(180deg,#b9cfe0 0%,#8f9c78 45%,#b4ad72 100%)}
.photo{position:absolute;left:63px;top:0;width:620px;height:458px;
  background:linear-gradient(180deg,#a9cbe8 0%,#8fa27a 45%,#c1b878 100%)}

.price-tag{position:absolute;left:0;top:102px;width:160px;height:84px;overflow:visible}
.price{position:absolute;left:10px;top:123px;font:600 32px/1 'Oswald',sans-serif;color:var(--white);text-shadow:0 2px 3px rgba(0,0,0,.6)}

.tag-bar{position:absolute;left:0;top:589px;width:746px;height:46px}
.tag-label{position:absolute;top:609px;font:700 14px/1 'Play',sans-serif;color:var(--white);letter-spacing:.3px;text-shadow:0 1px 2px rgba(0,0,0,.6)}
.tag-label.left{left:12px}
.tag-label.right{right:18px}
.disciplines{position:absolute;left:187px;width:370px;top:614px;text-align:center;font:700 10.5px/1 'Play',sans-serif;color:var(--cream);letter-spacing:.8px}

.footer{position:absolute;left:0;top:634px;width:746px;height:94px;background:linear-gradient(180deg,var(--wood),var(--wood-dark) 60%,var(--wood))}
.brand{position:absolute;left:36px;top:28px;display:flex;align-items:center;gap:8px}
.brand-mark{width:30px;height:30px;border-radius:50%;background:var(--cream)}
.brand-name{font:700 22px/1 'Play',sans-serif;color:var(--cream)}
.brand-url{position:absolute;left:54px;top:66px;font:700 9.5px/1 'Play',sans-serif;color:var(--cream);letter-spacing:.3px}
.block{position:absolute;text-align:center;font-family:'Play',sans-serif;font-weight:700}
.block h2{font-size:17px;color:var(--cream);letter-spacing:1px;line-height:1}
.block .name{font-size:14px;color:var(--accent);margin-top:4px;line-height:1}
.block p{font-size:11px;color:var(--white);margin-top:5px;line-height:1;letter-spacing:.5px}
.contact{left:258px;width:230px;top:10px}
.location{left:510px;width:222px;top:16px}

.strip{position:absolute;left:0;top:728px;width:746px;height:18px;background:var(--wood-dark);border-top:1px dashed #7a5436}
.listing{position:absolute;left:10px;top:3px;font:700 10px/1 'Oswald',sans-serif;color:var(--white)}
.copyright{position:absolute;left:61px;top:5px;font:700 6.5px/1 'Play',sans-serif;color:var(--white)}
.no-alter{position:absolute;right:7px;top:4px;font:700 6px/1 'Play',sans-serif;color:var(--white);border:1px solid var(--white);padding:1px 2px}
</style>
</head>
<body>
<div class="canvas">
  <svg width="0" height="0" style="position:absolute">
    <defs>
      <radialGradient id="leatherFill" cx=".5" cy=".45" r=".75">
        <stop offset="0" stop-color="#94532e"/>
        <stop offset=".65" stop-color="#7c4627"/>
        <stop offset="1" stop-color="#5f321a"/>
      </radialGradient>
      <filter id="leatherGrain" x="-5%" y="-5%" width="110%" height="110%">
        <feTurbulence type="fractalNoise" baseFrequency="0.9" numOctaves="4" seed="7" result="fine"/>
        <feColorMatrix in="fine" type="matrix" values="0 0 0 0 0.16  0 0 0 0 0.08  0 0 0 0 0.03  0 0 0 -2.2 1.35" result="pores"/>
        <feTurbulence type="fractalNoise" baseFrequency="0.025" numOctaves="3" seed="2" result="coarse"/>
        <feColorMatrix in="coarse" type="matrix" values="0 0 0 0 0.22  0 0 0 0 0.1  0 0 0 0 0.04  0 0 0 -1.4 0.85" result="mottle"/>
        <feComposite in="pores" in2="SourceGraphic" operator="in" result="poresIn"/>
        <feComposite in="mottle" in2="SourceGraphic" operator="in" result="mottleIn"/>
        <feGaussianBlur in="SourceAlpha" stdDeviation="3" result="blur"/>
        <feComposite in="SourceAlpha" in2="blur" operator="out" result="edge"/>
        <feFlood flood-color="#2a1409" flood-opacity=".55"/>
        <feComposite in2="edge" operator="in" result="edgeShade"/>
        <feMerge>
          <feMergeNode in="SourceGraphic"/>
          <feMergeNode in="mottleIn"/>
          <feMergeNode in="poresIn"/>
          <feMergeNode in="edgeShade"/>
        </feMerge>
      </filter>
      <filter id="tagShadow" x="-5%" y="-5%" width="115%" height="120%">
        <feDropShadow dx="1" dy="2" stdDeviation="1.5" flood-color="#000" flood-opacity=".45"/>
      </filter>
    </defs>
  </svg>

  <svg class="tag-sample tag-top" viewBox="0 0 356 175">
    <rect x="0" y="0" width="356" height="175" fill="url(#leatherFill)" filter="url(#leatherGrain)"/>
    <rect x="7.5" y="7.5" width="341" height="160" fill="none" stroke="#b8754a" stroke-opacity=".45" stroke-width="1"/>
    <rect x="7" y="7" width="342" height="161" fill="none" stroke="#2a1409" stroke-width="1.6" stroke-dasharray="4 2"/>
    <rect x="13" y="13" width="330" height="149" fill="none" stroke="#4a2612" stroke-width="1.2"/>
    <rect x="14" y="14" width="328" height="147" fill="none" stroke="#b8754a" stroke-opacity=".35" stroke-width="1"/>
  </svg>

  <svg class="tag-sample tag-left" viewBox="0 0 357 174">
    <path d="M0 0 H232 A125 100 0 0 1 357 100 V174 H0 Z" fill="url(#leatherFill)" filter="url(#leatherGrain)"/>
    <path d="M7 7 H232 A118 93 0 0 1 350 100 V167 H7 Z" fill="none" stroke="#2a1409" stroke-width="1.6" stroke-dasharray="4 2"/>
    <path d="M13 13 H232 A112 87 0 0 1 344 100 V161 H13 Z" fill="none" stroke="#4a2612" stroke-width="1.2"/>
    <path d="M14 14 H232 A111 86 0 0 1 343 100 V160 H14 Z" fill="none" stroke="#b8754a" stroke-opacity=".35" stroke-width="1"/>
  </svg>

  <svg class="tag-sample tag-right" viewBox="0 0 357 174">
    <path d="M357 0 H125 A125 100 0 0 0 0 100 V174 H357 Z" fill="url(#leatherFill)" filter="url(#leatherGrain)"/>
    <path d="M350 7 H125 A118 93 0 0 0 7 100 V167 H350 Z" fill="none" stroke="#2a1409" stroke-width="1.6" stroke-dasharray="4 2"/>
    <path d="M344 13 H125 A112 87 0 0 0 13 100 V161 H344 Z" fill="none" stroke="#4a2612" stroke-width="1.2"/>
    <path d="M343 14 H125 A111 86 0 0 0 14 100 V160 H343 Z" fill="none" stroke="#b8754a" stroke-opacity=".35" stroke-width="1"/>
  </svg>

  <section class="ad">
    <div class="photo-wrap">
      <div class="photo" role="img" aria-label="Photo of the bay broodmare in halter standing in a grassy field with trees and sky"></div>
    </div>

    <header class="header">
      <h1 class="reg-name">REGISTERED NAME</h1>
      <div class="horse-desc">2020 SORREL BROODMARE</div>
      <div class="lte" style="top:62px">LTE $XX,XXX</div>
      <div class="lte" style="top:80px">LTE $XX,XXX</div>

      <div class="ped parent lbl" style="top:34px">SIRE</div>
      <div class="ped parent" style="top:48px">LTE $XX,XXX</div>
      <div class="ped parent" style="top:62px">LTE $XX,XXX</div>
      <div class="ped parent lbl" style="top:95px">DAM</div>
      <div class="ped parent" style="top:110px">LTE $XX,XXX</div>
      <div class="ped parent" style="top:124px">LTE $XX,XXX</div>

      <div class="ped gp" style="top:24px">SIRE’S SIRE</div>
      <div class="ped-line" style="left:493px;width:123px;top:40px"></div>
      <div class="ped gp" style="top:44px">SIRE’S DAM</div>
      <div class="ped gp" style="top:85px">DAM’S SIRE</div>
      <div class="ped-line" style="left:493px;width:123px;top:101px"></div>
      <div class="ped gp" style="top:105px">DAM’S DAM</div>

      <div class="ped ggp" style="top:15px">SIRE’S SIRE’S SIRE</div>
      <div class="ped-line" style="left:626px;width:106px;top:26px"></div>
      <div class="ped ggp" style="top:29px">SIRE’S SIRE’S DAM</div>
      <div class="ped ggp" style="top:44px">SIRE’S DAM’S SIRE</div>
      <div class="ped-line" style="left:626px;width:106px;top:55px"></div>
      <div class="ped ggp" style="top:59px">SIRE’S DAM’S DAM</div>
      <div class="ped ggp" style="top:76px">DAM’S SIRE’S SIRE</div>
      <div class="ped-line" style="left:626px;width:106px;top:87px"></div>
      <div class="ped ggp" style="top:90px">DAM’S SIRE’S DAM</div>
      <div class="ped ggp" style="top:105px">DAM’S DAM’S SIRE</div>
      <div class="ped-line" style="left:626px;width:106px;top:116px"></div>
      <div class="ped ggp" style="top:119px">DAM’S DAM’S DAM</div>
    </header>
    <svg class="torn" viewBox="0 0 746 14" preserveAspectRatio="none">
      <path d="M0 0 H746 V6 L730 8 L712 5 L690 9 L668 6 L650 8 L628 5 L604 9 L580 6 L560 8 L536 5 L512 9 L490 6 L470 8 L448 5 L424 9 L400 6 L380 8 L356 5 L332 9 L310 6 L290 8 L266 5 L242 9 L220 6 L200 8 L176 5 L152 9 L130 6 L110 8 L86 5 L62 9 L40 6 L20 8 L0 5 Z" fill="#e4d8bb"/>
    </svg>

    <svg class="price-tag" viewBox="0 0 160 84">
      <g filter="url(#tagShadow)">
        <rect x="0" y="0" width="160" height="84" fill="url(#leatherFill)" filter="url(#leatherGrain)"/>
      </g>
      <path d="M0 5 H155 V79 H0" fill="none" stroke="#2a1409" stroke-width="1.4" stroke-dasharray="4 2"/>
      <path d="M0 9 H151 V75 H0" fill="none" stroke="#4a2612" stroke-width="1"/>
    </svg>
    <div class="price">$ 300.000</div>

    <svg class="tag-bar" viewBox="0 0 746 46">
      <rect x="150" y="16" width="446" height="30" fill="#6a391e" filter="url(#leatherGrain)"/>
      <line x1="180" y1="20" x2="566" y2="20" stroke="#2a1409" stroke-dasharray="4 2"/>
      <line x1="180" y1="42" x2="566" y2="42" stroke="#2a1409" stroke-dasharray="4 2"/>
      <path d="M0 0 H140 A47 46 0 0 1 187 46 H0 Z" fill="url(#leatherFill)" filter="url(#leatherGrain)"/>
      <path d="M0 4 H140 A43 42 0 0 1 183 46" fill="none" stroke="#2a1409" stroke-width="1.3" stroke-dasharray="4 2"/>
      <path d="M746 0 H604 A47 46 0 0 0 557 46 H746 Z" fill="url(#leatherFill)" filter="url(#leatherGrain)"/>
      <path d="M746 4 H604 A43 42 0 0 0 561 46" fill="none" stroke="#2a1409" stroke-width="1.3" stroke-dasharray="4 2"/>
    </svg>
    <div class="tag-label left">FOAL INCENTIVES</div>
    <div class="disciplines">DISCIPLINES: DISCIPLINE 1, DISCIPLINE 2, DISCIPLINE 3</div>
    <div class="tag-label right">DAM PICTURED</div>

    <footer class="footer">
      <div class="brand"><span class="brand-mark"></span><span class="brand-name">HARROW HORSE</span></div>
      <div class="brand-url">WWW.HARROWHORSE.COM</div>
      <div class="block contact">
        <h2>CONTACT</h2>
        <div class="name">FIRST NAME LAST NAME</div>
        <p>(000) 000-0000</p>
        <p>EMAIL@EMAIL.COM</p>
      </div>
      <div class="block location">
        <h2>LOCATION</h2>
        <div class="name">CITY, STATE</div>
        <p>TRANSPORT: BUYERS EXPENSE</p>
      </div>
    </footer>

    <div class="strip">
      <span class="listing">L#00000</span>
      <span class="copyright">COPYRIGHT © HARROW HORSE, LLC.</span>
      <span class="no-alter">DO NOT ALTER</span>
    </div>
  </section>
</div>
</body>
</html>
```